Stationary Set and Logo Update **PAYMENT GUARANTEED**

Stationery Design and Logo Update

About Us

Printvane Supply is a wholesale distributor of OEM [original brand] and compatible [generic brand] parts and supplies for use in copiers, faxes, printers, and multi-function machines. In plain English…we sell all the parts and supplies [such as toner] that make up any office equipment which outputs an image on paper.

Printvane was the 1st distributor to develop and sell a generic brand copier part in the United States. We have been in business since 1972 [nearly 40 years]. Our tagline is "The Steady Choice," as in our company was the first alternative product that copier dealers had to buying original brand copier parts. Printvane is known for offering reliable and cost-effective OEM and compatible products.

Project

We require a fresh, modern and corporate identity. Please submit a stationary package inclusive of a double-sided business card (2" x 3.5"), letterhead (8.5'x11"), and standard #10 envelope (4-1/8” x 9-1/2). You may use our current logo or preferably your take on an updated one. If an attempt is made in updating the logo #004D8E or a similar hue should be used as the primary color.

The design should be clean, simple, modern and professional and make an immediate impact.

Target Market(s)

Copier and printer dealers who lease and service imaging equipment in the United States and Latin America.

Industry/Entity Type

Business

Requirements
Must have
• Simple, clean, modern and professional. Please use #004D8E or a similar hue as the primary color. Letterhead must accommate (2) addresses. We have 2 locations.
Nice to have
• A simple, modern update to our current logo. https://media.brightlodgehost.example/fs030/5208846317720/img/418.jpg
Should not have
• More than (2) colors on logo.

```html
<!DOCTYPE html>
<html lang="en">
<head>
<meta charset="utf-8">
<title>Printvane Supply – Business Card</title>
<link href="https://fonts.googleapis.com/css2?family=Arimo:wght@400;700&display=swap" rel="stylesheet">
<style>
  :root {
    --backdrop: #7dbcf0;
    --card: #f2f2f3;
    --brand-blue: #0a4d96;
    --accent-cyan: #1fb2e8;
    --ink: #2a2a2a;
    --ink-soft: #3c3c3c;
  }
  * { margin: 0; padding: 0; box-sizing: border-box; }
  html, body {
    width: 1200px; height: 720px; overflow: hidden;
    background: var(--backdrop);
    font-family: "Arimo", Arial, sans-serif;
  }
  .canvas { position: relative; width: 1200px; height: 720px; }
  .card {
    position: absolute; top: 144px;
    width: 548px; height: 330px;
    background: var(--card);
    border-radius: 16px;
  }
  .card--front { left: 48px; }
  .card--back { left: 604px; }

  .logo {
    position: absolute; display: flex; align-items: center;
  }
  .logo__dot {
    border-radius: 50%; background: var(--accent-cyan); flex: none;
  }
  .logo__name {
    font-weight: 700; color: var(--brand-blue); letter-spacing: -0.5px; line-height: 1;
  }
  .logo__url {
    position: absolute; font-weight: 700; color: var(--ink); white-space: nowrap;
  }

  .card--front .logo { left: 110px; top: 128px; }
  .card--front .logo__dot { width: 42px; height: 42px; margin-right: 12px; }
  .card--front .logo__name { font-size: 62px; }
  .card--front .logo__url { right: 2px; top: 70px; font-size: 12px; }

  .card--back .logo { right: 22px; top: 40px; }
  .card--back .logo__dot { width: 22px; height: 22px; margin-right: 7px; }
  .card--back .logo__name { font-size: 32px; }
  .card--back .logo__url { right: 0; top: 36px; font-size: 8px; }

  .person { position: absolute; left: 22px; top: 54px; color: var(--ink); }
  .person__name { font-size: 17px; }
  .person__title { font-size: 12px; margin-top: 4px; }

  .office {
    position: absolute; top: 180px;
    font-size: 13px; line-height: 22px; color: var(--ink-soft);
  }
  .office--main { left: 22px; }
  .office--west { right: 22px; text-align: right; }
</style>
</head>
<body>
<main class="canvas">
  <section class="card card--front" aria-label="Business card front">
    <div class="logo">
      <span class="logo__dot"></span>
      <span class="logo__name">Printvane</span>
      <span class="logo__url">www.printvane.example</span>
    </div>
  </section>

  <section class="card card--back" aria-label="Business card back">
    <div class="person">
      <p class="person__name">Lena Marwick</p>
      <p class="person__title">Director</p>
    </div>
    <div class="logo">
      <span class="logo__dot"></span>
      <span class="logo__name">Printvane</span>
      <span class="logo__url">www.printvane.example</span>
    </div>
    <address class="office office--main" style="font-style:normal">
      Corporate Office<br>
      2280 Harborline Avenue<br>
      Coral Bend, FL 33420<br>
      Toll Free: 800.555.0140<br>
      Local: 954.555.0172<br>
      Fax: 954.555.0188
    </address>
    <address class="office office--west" style="font-style:normal">
      Printvane West<br>
      West Coast Fulfillment Center<br>
      Sage Ridge Commerce Park #4<br>
      940 Talon Way, Reno, NV 89502<br>
      Toll Free: 800.555.0166<br>
      Fax: 775.555.0129
    </address>
  </section>
</main>
</body>
</html>
```